Power Washing Business Easy Postcard Design

We need a postcard designed for our company, which does residential power washing. We clean houses, decks, driveways and fences. The design should be understated, high end with minimalist graphics. No bubbles or wild colors. The name of the business is "stoneridge power washing" which should be rendered all lower case in a san serif font. Sample files in blue or white are attached. The attached files aren't our logo, just a model. The font doesn't have to be exact and "power washing" needs to be added to it.The postcard size is the Marlo Press 8.64" X 5.59". The photo which is attached should fill the whole front of the card.

The text elements on the front are:
1) "stoneridge power washing"- as per the attached files, can be broken into two lines

2) "Mention this card and receive a FREE standard size Deck Wash"

3) "804-555-3186"

4) "stoneridgepowerwashing.example" (this font size can be smaller than the phone number.)

5)"We Clean:- Houses- Decks- Driveways- Fences"The arrangement is the text is up to you. The text should not overpower the image.

Target Market(s)

Homeowners

Industry/Entity Type

Residential

Font styles to use
Sans Serif

Requirements
Should not have
• Garish graphics

```html
<!DOCTYPE html>
<html lang="en">
<head>
<meta charset="utf-8">
<title>stoneridge power washing – postcard</title>
<link rel="stylesheet" href="https://fonts.googleapis.com/css2?family=Lato:wght@400;700;900&family=Lora:wght@600;700&display=swap">
<style>
  :root {
    --navy: #1d1f4e;
    --red: #d7121b;
    --red-deep: #b50d16;
    --white: #ffffff;
    --ink: #24264f;
    --canvas: #e6e6e6;
    --paper: #f7f7f7;
    --rule: #1a1a1a;
    --sky-top: #5a78b8;
    --sky-low: #b9c3d8;
    --lawn: #4e7a2e;
  }
  * { box-sizing: border-box; margin: 0; padding: 0; }
  html, body { width: 800px; height: 1200px; overflow: hidden; }
  body { background: var(--canvas); position: relative; font-family: "Lato", sans-serif; }

  .card { position: absolute; left: 65px; width: 663px; overflow: hidden; box-shadow: 0 2px 8px rgba(0,0,0,.18); }
  .card--front { top: 46px; height: 513px; }
  .card--back { top: 618px; height: 512px; background: var(--paper); }

  .front-photo {
    position: absolute; inset: 0;
    background: linear-gradient(180deg, var(--sky-top) 0%, var(--sky-low) 30%, #8a8e99 45%, #6b6a66 58%, var(--lawn) 72%, #3d6224 100%);
  }
  .front-shapes { position: absolute; inset: 0; width: 663px; height: 513px; }

  .web-address {
    position: absolute; top: 20px; right: 18px;
    font: 700 14px "Lato", sans-serif; color: var(--ink);
  }

  .brand { position: absolute; text-align: center; color: var(--white); }
  .brand--front { left: 405px; top: 228px; width: 176px; }
  .brand__name { font: 900 30px/1 "Lato", sans-serif; letter-spacing: -0.3px; }
  .brand__tag {
    margin-top: 5px; padding-top: 4px; border-top: 1.5px solid currentColor;
    font: 400 13px/1 "Lato", sans-serif; letter-spacing: 1px;
  }

  .services { position: absolute; left: 24px; top: 282px; width: 360px; color: var(--white); text-align: center; }
  .services__title { font: 700 23px/1 "Lora", serif; letter-spacing: .5px; }
  .services__list {
    margin-top: 10px; padding-bottom: 7px; border-bottom: 2px solid var(--white);
    font: 700 16px/1 "Lato", sans-serif; white-space: nowrap;
  }
  .services__list .dot { color: var(--red); margin: 0 3px; }

  .call { position: absolute; left: 130px; top: 348px; white-space: nowrap; display: flex; align-items: center; gap: 6px; }
  .call__icon { width: 16px; height: 16px; }
  .call__label { font: 700 16px "Lora", serif; color: var(--red); text-transform: uppercase; }
  .call__number { font: 900 21px "Lato", sans-serif; color: var(--white); }

  .offer { position: absolute; left: 31px; top: 434px; width: 603px; text-align: center; }
  .offer__lead {
    font: 700 14px/1 "Lato", sans-serif; color: var(--navy); letter-spacing: 9.4px; text-transform: uppercase;
    padding-bottom: 6px; border-bottom: 1.5px solid var(--navy); white-space: nowrap;
  }
  .offer__main { margin-top: 8px; font: 700 29px/1 "Lora", serif; color: var(--white); text-transform: uppercase; white-space: nowrap; }

  .back-photo {
    position: absolute; left: 0; right: 0; top: 70px; bottom: 0;
    background: linear-gradient(180deg, #f4f4f4 0%, #e4e4e4 40%, #dcdcdc 70%, #ececec 100%);
    opacity: .8;
  }
  .brand--back { left: 37px; top: 46px; text-align: left; color: var(--navy); }
  .brand--back .brand__name { font-size: 23px; }
  .brand--back .brand__tag { font-size: 11px; margin-top: 4px; padding-top: 3px; letter-spacing: .8px; }

  .stamp-box { position: absolute; left: 531px; top: 50px; width: 88px; height: 110px; border: 1.5px solid var(--rule); background: var(--white); }
  .address-lines { position: absolute; left: 371px; top: 338px; width: 249px; }
  .address-lines span { display: block; height: 42px; border-top: 1.5px solid var(--rule); }
</style>
</head>
<body>
  <section class="card card--front">
    <div class="front-photo" role="img" aria-label="Two-storey suburban house with grey siding, lit porch and green lawn at dusk"></div>

    <svg class="front-shapes" viewBox="0 0 663 513" aria-hidden="true">
      <defs>
        <linearGradient id="redBand" x1="0" y1="0" x2="1" y2="0">
          <stop offset="0" stop-color="var(--red-deep)"/>
          <stop offset=".5" stop-color="var(--red)"/>
          <stop offset="1" stop-color="var(--red-deep)"/>
        </linearGradient>
      </defs>
      <path d="M663,112 C560,118 440,160 410,240 C398,300 380,345 300,372 C200,390 100,388 0,380 L0,388 C200,400 420,396 663,282 Z" fill="var(--navy)"/>
      <circle cx="500" cy="250" r="118" fill="none" stroke="var(--navy)" stroke-width="1.4"/>
      <circle cx="504" cy="254" r="125" fill="none" stroke="var(--navy)" stroke-width="1"/>
      <path d="M0,388 C200,400 420,396 663,282 L663,322 C420,440 200,420 0,404 Z" fill="var(--white)"/>
      <path d="M0,404 C200,420 420,440 663,322 L663,513 L0,513 Z" fill="url(#redBand)"/>
    </svg>

    <p class="web-address">www.stoneridgepowerwashing.example</p>

    <div class="brand brand--front">
      <p class="brand__name">stoneridge</p>
      <p class="brand__tag">POWER WASHING</p>
    </div>

    <div class="services">
      <p class="services__title">WE CLEAN</p>
      <p class="services__list"><span class="dot">•</span>HOUSES<span class="dot">•</span>DECKS<span class="dot">•</span>DRIVEWAYS<span class="dot">•</span>FENCES</p>
    </div>

    <p class="call">
      <svg class="call__icon" viewBox="0 0 24 24" aria-hidden="true"><path fill="var(--red)" d="M6.6 10.8c1.4 2.8 3.8 5.1 6.6 6.6l2.2-2.2c.3-.3.7-.4 1-.2 1.1.4 2.3.6 3.6.6.6 0 1 .4 1 1V20c0 .6-.4 1-1 1C10.6 21 3 13.4 3 4c0-.6.4-1 1-1h3.5c.6 0 1 .4 1 1 0 1.3.2 2.5.6 3.6.1.3 0 .7-.2 1z"/></svg>
      <span class="call__label">Call us</span>
      <span class="call__number">804-555-3186</span>
    </p>

    <div class="offer">
      <p class="offer__lead">Mention this card and receive</p>
      <p class="offer__main">A free standard size deck wash</p>
    </div>
  </section>

  <section class="card card--back">
    <div class="back-photo" role="img" aria-label="Faded view of the two-storey house with garage and driveway"></div>
    <div class="brand brand--back">
      <p class="brand__name">stoneridge</p>
      <p class="brand__tag">POWER WASHING</p>
    </div>
    <div class="stamp-box"></div>
    <div class="address-lines"><span></span><span></span><span></span></div>
  </section>
</body>
</html>
```